TRVL-NINE Web Design

We are a Health, Safety, Environmental & Quality Recruitment Agency, our clients are major corporate Mining, Oil & Gas and Engineering companies. We have offices in Perth & Melbourne, Australia

The website should be very functional & easy to navigate

BUT REALLY LOOKING FOR WOW FACTOR!

Please Note: TRVL CORPORATE IS OUR OLD COMPANY THE NEW ONE IS "TRVL-NINE" 

Some idea's from our competitors:

http://www.guardlinepeak.com.au/
http://www.vantagehiring.com.au/
http://www.brightpick.com.au/
http://www.kovastaffing.co.uk/
http://www.jobmarrow.com/health-safety-environment-jobs

Would love to see some of our valued clients and there logos

still looking for wow factor

Industry/Entity Type

Mining

Requirements
Must have
• A place where candidates can upload there resumes & other contact details
• eg: http://www.guardlinepeak.com.au/candidates/register-your-resume/
• A place we can load jobs on to eg: http://www.guardlinepeak.com.au/vacancies/
• Contact details:
• Perth: 12 Kestrel Ave, West Perth, Western Australia 6005
• t: 08 7153 4406 | f: 08 7153 4470 |
• Melbourne: Level 1, 218 Arbour Lane, Melbourne, Victoria 3000
• t: 03 6214 5072| f: 03 6231 4095 |
• e: dennisk@trvlnine.com.au | w: http://www.trvlnine.com.au

```html
<!DOCTYPE html>
<html lang="en">
<head>
<meta charset="utf-8">
<title>TRVL NINE – Health, Safety, Environment &amp; Quality Recruitment</title>
<link rel="stylesheet" href="https://fonts.googleapis.com/css2?family=Lato:ital,wght@0,300;0,400;0,700;1,400&family=Ropa+Sans&display=swap">
<style>
:root{
  --nav-bg:#4b4f53;
  --nav-active:#3c3f43;
  --text-dark:#333638;
  --text-mid:#6b6e70;
  --text-light:#9a9da0;
  --brand-blue:#1a6fc9;
  --brand-blue-dark:#0f4f96;
  --band-blue:#1f78d6;
  --section-grey:#efefef;
  --line-grey:#dcdcdc;
  --accent-orange:#f0822a;
  --footer-bg:#56595d;
  --footer-line:#65686c;
  --base-bg:#393c3f;
  --white:#ffffff;
}
*{box-sizing:border-box;margin:0;padding:0}
html,body{width:810px;height:1200px;overflow:hidden}
body{font-family:"Lato",Arial,sans-serif;color:var(--text-dark);background:var(--white);position:relative}
.heading-font{font-family:"Ropa Sans","Arial Narrow",sans-serif;font-weight:400}
h1,h2,h3{font-weight:400}
a{color:inherit;text-decoration:none}

/* top navigation */
.top-nav{position:absolute;top:0;left:0;width:810px;height:20px;background:var(--nav-bg)}
.top-nav ul{list-style:none;position:absolute;right:107px;top:0;display:flex;height:20px}
.top-nav li{font-size:9px;color:#e4e5e6;line-height:20px;padding:0 12px;border-left:1px solid #5a5e62}
.top-nav li:first-child{border-left:none}
.top-nav li.is-active{background:var(--nav-active);color:var(--white)}

/* header */
.site-header{position:absolute;top:20px;left:0;width:810px;height:65px;background:var(--white)}
.brand{position:absolute;left:110px;top:12px;display:flex;align-items:center;gap:8px}
.brand-mark{width:40px;height:40px;background:#6f7478;border-radius:3px}
.brand-name{font-size:20px;font-weight:300;color:#5f6468;letter-spacing:.5px}
.call-box{position:absolute;right:190px;top:20px;display:flex;align-items:center;gap:5px;white-space:nowrap}
.call-icon{width:24px;height:24px;margin-right:2px}
.call-label{font-size:10.5px;font-style:italic;color:var(--text-mid)}
.call-number{font-size:13px;font-weight:700;color:var(--brand-blue)}
.social{position:absolute;left:628px;top:21px;display:flex;gap:4px}
.social span{width:22px;height:22px;background:#e3e3e3;border-radius:2px;display:block}

/* hero */
.hero{position:absolute;top:85px;left:0;width:810px;height:280px;
  background:linear-gradient(180deg,#0c1f3c 0%,#1e3a63 45%,#33557e 70%,#5c5030 86%,#0b0b0b 100%)}
.hero-caption{position:absolute;top:365px;left:0;width:810px;height:50px;
  background:linear-gradient(180deg,var(--band-blue),#1866bd)}
.hero-caption p{position:absolute;left:0;width:810px;top:14px;text-align:center;color:var(--white);font-size:17px}
.slider-arrow{position:absolute;top:11px;width:28px;height:28px}
.slider-arrow.prev{left:108px}
.slider-arrow.next{left:674px}

/* welcome */
.welcome{position:absolute;top:415px;left:0;width:810px;height:333px;background:var(--section-grey);border-bottom:1px solid #e0e0e0}
.welcome h1{position:absolute;top:26px;width:810px;text-align:center;font-size:24px;color:var(--text-dark)}
.welcome .intro{position:absolute;top:57px;left:125px;width:560px;text-align:center;font-size:12.5px;line-height:16px;color:var(--brand-blue)}
.welcome .divider{position:absolute;top:100px;left:235px;width:340px;height:14px}
.feature{position:absolute;top:140px;width:156px;height:156px;border-radius:50%;overflow:hidden;border:4px solid #dfe3ea;box-shadow:0 2px 4px rgba(0,0,0,.15)}
.feature.positions{left:108px;background:linear-gradient(160deg,#9fc3e6,#6d89a8 55%,#2c3f66)}
.feature.candidates{left:327px;background:linear-gradient(160deg,#5a3a57,#a66a4a 50%,#2a2540)}
.feature.employers{left:546px;background:linear-gradient(160deg,#8ab5de,#c96a36 55%,#203b6e)}
.feature .label{position:absolute;top:62px;left:0;width:100%;height:30px;background:rgba(30,30,30,.82);color:var(--white);font-size:15px;line-height:30px;text-align:center}

/* jobs */
.jobs-title{position:absolute;top:781px;left:108px;font-size:16px;color:var(--text-dark)}
.sort{position:absolute;top:783px;left:363px;display:flex;align-items:center;gap:6px;font-size:8.5px;color:var(--text-mid)}
.sort .select{width:84px;height:17px;border:1px solid #cfcfcf;border-radius:2px;background:linear-gradient(#fff,#f0f0f0);font-size:8.5px;color:var(--text-dark);line-height:15px;padding-left:7px;position:relative}
.sort .select::after{content:"";position:absolute;right:7px;top:6px;border:3px solid transparent;border-top-color:#444}
.job-table{position:absolute;top:809px;left:108px;width:375px;border:1px solid var(--line-grey);border-collapse:collapse;background:#f6f6f6;font-size:8.5px}
.job-table th{height:20px;background:#e8e8e8;text-align:left;font-weight:700;color:var(--text-dark);padding-left:8px}
.job-table td{height:28px;padding-left:8px;color:var(--text-dark);border-top:1px solid #e6e6e6}
.apply-btn{display:block;width:55px;height:16px;background:var(--brand-blue);color:var(--white);font-weight:700;font-size:8.5px;text-align:center;line-height:16px;border-radius:1px}

/* upload */
.upload-title{position:absolute;top:781px;left:510px;font-size:16px;color:var(--text-dark)}
.upload-form{position:absolute;top:809px;left:510px;width:192px;height:169px;background:#eeeeee;border:1px solid var(--line-grey)}
.field{position:absolute;left:12px;width:167px;height:21px;background:var(--white);border:1px solid #dadada;border-radius:2px;font-size:8.5px;color:var(--text-light);line-height:19px;padding-left:19px}
.field svg{position:absolute;left:6px;top:5px}
.file-row{position:absolute;left:12px;top:93px;display:flex;align-items:center;gap:8px;font-size:8.5px;color:var(--text-mid)}
.file-btn{width:84px;height:18px;border:1px solid #c8c8c8;border-radius:2px;background:linear-gradient(#fafafa,#e6e6e6);color:var(--text-dark);text-align:center;line-height:16px}
.upload-btn{position:absolute;left:12px;top:130px;width:167px;height:26px;background:var(--accent-orange);color:var(--white);font-size:12.5px;text-align:center;line-height:26px;border-radius:1px}

/* footer */
.site-footer{position:absolute;top:1014px;left:0;width:810px;height:131px;background:var(--footer-bg)}
.footer-col{position:absolute;top:20px;height:95px}
.footer-col + .footer-col{border-left:1px solid var(--footer-line)}
.footer-col h3{font-size:12px;color:var(--white);display:flex;align-items:center;gap:5px;margin-bottom:6px}
.footer-col ul{list-style:none}
.footer-col li{font-size:8px;color:#d8d9da;line-height:14.5px;padding-left:8px;position:relative}
.footer-col li::before{content:"";position:absolute;left:0;top:6px;width:3px;height:3px;background:#8f9295}
.footer-col li.is-current{color:var(--white)}
.newsletter p{font-size:8px;font-style:italic;color:#d0d2d4;line-height:12px;width:140px}
.news-input{position:absolute;top:53px;left:0;width:160px;height:21px;background:var(--white);border-radius:2px;font-size:8px;font-style:italic;color:var(--text-light);line-height:21px;padding-left:7px}
.news-go{position:absolute;right:3px;top:3px;width:16px;height:15px;background:var(--brand-blue);border-radius:2px}
.site-base{position:absolute;top:1145px;left:0;width:810px;height:55px;background:var(--base-bg);text-align:center}
.site-base p{font-size:8px;color:#c9cbcd;margin-top:16px}
.site-base small{display:block;font-size:8px;color:#8e9194;margin-top:5px}
.site-base strong{color:#d9dadb;font-weight:400}
</style>
</head>
<body>

<nav class="top-nav">
  <ul>
    <li class="is-active">Home</li>
    <li>About Us</li>
    <li>Position We Offer</li>
    <li>Candidates</li>
    <li>Employers</li>
    <li>Contact</li>
  </ul>
</nav>

<header class="site-header">
  <div class="brand"><span class="brand-mark"></span><span class="brand-name">TRVL-NINE</span></div>
  <div class="call-box">
    <svg class="call-icon" viewBox="0 0 24 24"><circle cx="12" cy="12" r="11" fill="none" stroke="#c4c6c8" stroke-width="1.5"/><path d="M8.5 6.5c.8-.5 1.5 0 2 1l.8 1.8c.3.7 0 1.2-.6 1.6l-.6.4c.6 1.6 1.8 2.9 3.3 3.6l.5-.6c.4-.6 1-.8 1.6-.5l1.8.9c.9.5 1.2 1.2.7 2-.8 1.2-2 1.6-3.3 1.2-3.2-1-5.7-3.6-6.7-6.8-.4-1.3 0-2.6.5-3.6z" fill="#b5b8ba"/></svg>
    <span class="call-label">For more details call :</span>
    <span class="call-number">03 6214 5072</span>
  </div>
  <div class="social" aria-label="Social links"><span></span><span></span><span></span></div>
</header>

<section class="hero" role="img" aria-label="Night view of an industrial power station with cooling tower, chimneys and cranes lit against a deep blue sky"></section>
<div class="hero-caption">
  <svg class="slider-arrow prev" viewBox="0 0 28 28"><circle cx="14" cy="14" r="14" fill="#0f4a8c"/><path d="M16 8l-6 6 6 6" fill="none" stroke="#fff" stroke-width="2"/></svg>
  <p class="heading-font">Australia's number 1 Health, Safety, Environment and Quality recruitment group</p>
  <svg class="slider-arrow next" viewBox="0 0 28 28"><circle cx="14" cy="14" r="14" fill="#0f4a8c"/><path d="M12 8l6 6-6 6" fill="none" stroke="#fff" stroke-width="2"/></svg>
</div>

<section class="welcome">
  <h1 class="heading-font">Welcome to TRVL NINE</h1>
  <p class="intro">TRVL NINE is a Perth-based independent, specialised recruitment company with a focus on Health, Safety, Environment and Quality positions within the resources sector.</p>
  <svg class="divider" viewBox="0 0 340 14"><defs><linearGradient id="fade" x1="0" x2="1"><stop offset="0" stop-color="#e2e2e2" stop-opacity="0"/><stop offset=".5" stop-color="#dcdcdc"/><stop offset="1" stop-color="#e2e2e2" stop-opacity="0"/></linearGradient></defs><rect x="0" y="6" width="340" height="2" fill="url(#fade)"/><path d="M163 6h14l-7 7z" fill="#dcdcdc"/></svg>
  <div class="feature positions" role="img" aria-label="Engineer in a hard hat at a refinery plant"><span class="label heading-font">POSITIONS WE OFFER</span></div>
  <div class="feature candidates" role="img" aria-label="Welder at work with sparks"><span class="label heading-font">CANDIDATES</span></div>
  <div class="feature employers" role="img" aria-label="Two site workers in safety gear reviewing a clipboard"><span class="label heading-font">EMPLOYERS</span></div>
</section>

<h2 class="jobs-title heading-font">Apply our jobs</h2>
<div class="sort">Sort by : <div class="select">Health &amp; Safety</div></div>
<table class="job-table">
  <thead><tr><th style="width:158px">Job Title</th><th style="width:78px">Industry</th><th style="width:70px">Salary ($)</th><th></th></tr></thead>
  <tbody>
    <tr><td>Corporate Health &amp; Safety Managers</td><td>Health &amp; Safety</td><td>$ 0.00 - $0.00</td><td><a class="apply-btn">APPLY</a></td></tr>
    <tr><td>Emergency Response Professionals</td><td>Health &amp; Safety</td><td>$ 0.00 - $0.00</td><td><a class="apply-btn">APPLY</a></td></tr>
    <tr><td>Health &amp; Safety Coordinators</td><td>Health &amp; Safety</td><td>$ 0.00 - $0.00</td><td><a class="apply-btn">APPLY</a></td></tr>
    <tr><td>Health &amp; Safety Directors</td><td>Health &amp; Safety</td><td>$ 0.00 - $0.00</td><td><a class="apply-btn">APPLY</a></td></tr>
    <tr><td>Safety System Professionals</td><td>Health &amp; Safety</td><td>$ 0.00 - $0.00</td><td><a class="apply-btn">APPLY</a></td></tr>
  </tbody>
</table>

<h2 class="upload-title heading-font">Upload resumes &amp; other contact</h2>
<form class="upload-form">
  <div class="field" style="top:11px"><svg width="9" height="9" viewBox="0 0 9 9"><circle cx="4.5" cy="2.5" r="2" fill="#b3b3b3"/><path d="M0.5 9c0-2.5 1.8-4 4-4s4 1.5 4 4z" fill="#b3b3b3"/></svg>Your name</div>
  <div class="field" style="top:37px"><svg width="9" height="9" viewBox="0 0 9 9"><rect x=".5" y="1.5" width="8" height="6" fill="none" stroke="#b3b3b3"/><path d="M.5 1.5l4 3.5 4-3.5" fill="none" stroke="#b3b3b3"/></svg>Email address</div>
  <div class="field" style="top:63px"><svg width="9" height="9" viewBox="0 0 9 9"><circle cx="4.5" cy="4.5" r="4" fill="none" stroke="#b3b3b3"/><path d="M3 2.5l1 1.5-.6.6c.4.8 1 1.4 1.7 1.7l.6-.6 1.3 1" fill="none" stroke="#b3b3b3"/></svg>Phone No.</div>
  <div class="file-row"><span class="file-btn">Choose File</span>No File Chosen</div>
  <div class="upload-btn heading-font">UPLOAD NOW</div>
</form>

<footer class="site-footer">
  <div class="footer-col" style="left:108px;width:115px">
    <h3 class="heading-font"><svg width="10" height="12" viewBox="0 0 10 12"><rect x=".5" y="1.5" width="9" height="10" fill="none" stroke="#fff"/><rect x="3" y=".5" width="4" height="2" fill="#fff"/><path d="M2.5 5h5M2.5 7h5M2.5 9h5" stroke="#fff"/></svg>Main Menu</h3>
    <ul><li>About Us</li><li class="is-current">Position We Offer</li><li>Candidates</li><li>Employers</li><li>Contact</li></ul>
  </div>
  <div class="footer-col" style="left:223px;width:147px;padding-left:32px">
    <h3 class="heading-font"><svg width="10" height="12" viewBox="0 0 10 12"><path d="M3 1c.6 0 1 .4 1 1v5l1-1c.5-.4 1 0 1 .3l2 .7c.6.2 1 .8.8 1.4L8 11H4L1.5 7.5c-.3-.4 0-1 .6-.8L2 7V2c0-.6.4-1 1-1z" fill="none" stroke="#fff"/></svg>Get In Touch</h3>
    <ul><li>Facepage</li><li>Chirper</li><li>Linkwork</li></ul>
  </div>
  <div class="footer-col" style="left:370px;width:138px;padding-left:32px">
    <h3 class="heading-font"><svg width="12" height="12" viewBox="0 0 12 12"><path d="M5 7l2-2M4.5 5.5l-2 2a1.8 1.8 0 0 0 2.5 2.5l2-2M7.5 6.5l2-2A1.8 1.8 0 0 0 7 2L5 4" fill="none" stroke="#fff" stroke-width="1.3"/></svg>Useful Link</h3>
    <ul><li>Site Map</li><li>Private Policy</li><li>Term of Use</li></ul>
  </div>
  <div class="footer-col newsletter" style="left:508px;width:200px;padding-left:33px">
    <h3 class="heading-font">Newsletter Sign Up</h3>
    <p>Lorem ipsum dolor sit amet, consectetur adipiscing elit.</p>
    <div class="news-input" style="left:33px">Your Email Id...<svg class="news-go" viewBox="0 0 16 15"><rect width="16" height="15" rx="2" fill="#1a6fc9"/><path d="M4 4.5l3 3-3 3M8 4.5l3 3-3 3" fill="none" stroke="#fff" stroke-width="1.3"/></svg></div>
  </div>
</footer>

<div class="site-base">
  <p>Lorem ipsum dolor sit amet, consectetur adipiscing elit. Phasellus pretium varius consequat. Ut metus arcu, viverra in ultrices ac, pharetra non ante.</p>
  <small>© Copyright 2013, <strong>TRVL NINE</strong>. All Rights Reserved</small>
</div>

</body>
</html>
```